Business card design for international hub site

I need a business card design with the logo attached. Although the site is for the teenage audience (it is about the high school graduation ball, the Prom), the business card is for professional use to be given to professional contacts (B2B), such as suppliers and partners, so it needs to look professional (but also girly, glamours and clean).

Target Market(s)

B2B

Industry/Entity Type

Media

Colors
eea4c8
f9d9e8
e667a6
9d9d9d
1b1b1b

Requirements
Must have
• Space for Name, Tile, Address, Phone, email and website.
Should not have
• Photo

```html
<!DOCTYPE html>
<html lang="en">
<head>
<meta charset="utf-8">
<title>The Gown Hive – Business Card</title>
<link rel="stylesheet" href="https://fonts.googleapis.com/css2?family=EB+Garamond:ital,wght@0,400;0,500;0,700;1,400&family=Titillium+Web:wght@400&display=swap">
<style>
  :root {
    --card-dark: #434343;
    --pink: #e667a6;
    --pink-soft: #eea4c8;
    --grey: #9d9d9d;
    --grey-band: #8c8c8c;
    --ink: #1b1b1b;
    --white: #ffffff;
    --stage: #d2d2d2;
  }
  * { margin: 0; padding: 0; box-sizing: border-box; }
  html, body { width: 1200px; height: 1200px; overflow: hidden; }
  body {
    background: var(--stage);
    font-family: "EB Garamond", Georgia, serif;
    position: relative;
  }
  .card {
    position: absolute;
    left: 70px;
    width: 820px;
    height: 469px;
    background: var(--card-dark);
    overflow: hidden;
  }
  .card--front { top: 110px; }
  .card--back { top: 621px; }
  .card__swoosh {
    position: absolute;
    inset: 0;
    width: 820px;
    height: 469px;
  }
  .side-label {
    position: absolute;
    left: 930px;
    font-family: "Titillium Web", Arial, sans-serif;
    font-size: 46px;
    color: var(--ink);
    line-height: 1;
  }
  .side-label--front { top: 320px; }
  .side-label--back { top: 831px; }

  .brand {
    position: absolute;
    color: var(--pink);
    font-weight: 500;
    line-height: 1;
    white-space: nowrap;
  }
  .card--front .brand { left: 66px; top: 120px; font-size: 66px; }
  .card--back .brand { left: 0; right: 0; top: 170px; text-align: center; font-size: 92px; }

  .address {
    position: absolute;
    left: 66px;
    top: 318px;
    color: var(--white);
    font-size: 24px;
    line-height: 1.2;
  }
  .contact {
    position: absolute;
    right: 40px;
    top: 140px;
    text-align: right;
    color: var(--white);
  }
  .contact__name { font-size: 32px; font-weight: 700; line-height: 1.1; }
  .contact__title { font-size: 22px; font-style: italic; margin-bottom: 22px; }
  .contact__line {
    display: flex;
    justify-content: flex-end;
    align-items: center;
    gap: 8px;
    font-size: 23px;
    line-height: 1.4;
  }
  .contact__icon { width: 22px; height: 22px; flex: none; }
  .website {
    position: absolute;
    right: 24px;
    bottom: 16px;
    color: var(--white);
    font-size: 24px;
    font-weight: 700;
  }
</style>
</head>
<body>

  <section class="card card--front" aria-label="Card front">
    <svg class="card__swoosh" viewBox="0 0 820 469" aria-hidden="true">
      <path fill="var(--grey-band)" d="M260 432 Q580 412 820 330 L820 372 Q560 432 260 432 Z"/>
      <path fill="var(--pink)" d="M0 426 Q420 438 820 362 L820 469 L0 469 Z"/>
    </svg>
    <div class="brand">The Gown Hive</div>
    <p class="address">Unit, Street,<br>City, State, Zip</p>
    <div class="contact">
      <div class="contact__name">Name Here</div>
      <div class="contact__title">Title</div>
      <div class="contact__line">(000) 000-0000
        <svg class="contact__icon" viewBox="0 0 22 22" aria-hidden="true"><circle cx="11" cy="11" r="11" fill="var(--white)"/><rect x="7.5" y="4.5" width="7" height="13" rx="1.5" fill="none" stroke="var(--card-dark)" stroke-width="1.8"/></svg>
      </div>
      <div class="contact__line">(000) 000-0000
        <svg class="contact__icon" viewBox="0 0 22 22" aria-hidden="true"><circle cx="11" cy="11" r="11" fill="var(--white)"/><path d="M5 9 Q11 4 17 9 L15 11 L13 9 L9 9 L7 11 Z" fill="var(--card-dark)"/><rect x="7" y="11" width="8" height="6" rx="1" fill="var(--card-dark)"/></svg>
      </div>
      <div class="contact__line">name@thegownhive.com
        <svg class="contact__icon" viewBox="0 0 22 22" aria-hidden="true"><circle cx="11" cy="11" r="11" fill="var(--white)"/><rect x="5" y="7" width="12" height="8" fill="var(--card-dark)"/><path d="M5 7 L11 12 L17 7" fill="none" stroke="var(--white)" stroke-width="1.2"/></svg>
      </div>
    </div>
    <div class="website">www.thegownhive.com</div>
  </section>
  <div class="side-label side-label--front">Front</div>

  <section class="card card--back" aria-label="Card back">
    <svg class="card__swoosh" viewBox="0 0 820 469" aria-hidden="true">
      <path fill="var(--grey-band)" d="M260 416 Q580 396 820 330 L820 362 Q560 416 260 416 Z"/>
      <path fill="var(--pink)" d="M0 412 Q420 420 820 352 L820 469 L0 469 Z"/>
    </svg>
    <div class="brand">The Gown Hive</div>
  </section>
  <div class="side-label side-label--back">Back</div>

</body>
</html>
```